Patio Haven Appliances

we want our logo to be the full front of the card listing our address email and phone and for it to state at our address is a showroom. back of card list of appliances i listed below. Also want the QTR Logo, Chatterly Icon and Pixorama Icon on card

Industry/Entity Type

Outdoor appliances

Contact Information for Business Card

Front of card to show our logo, address and state under logo showroom under the addresslist of appliances we sell on back of card - Orvo, ZRE, Kelu, Quilo, Varno, Kestel, Stonewick, Bellardi, Gallivant, Ember Charm, Gray Whitfield, Coastal Blaze, Silver Herons

Requirements
Must have
• Our email (Info@Patiohavenqx.com) phone (555-302-1186), address,(87 Corvale Avenue Fernbrook, QX 11598) QTR Icon, CH Icon and PX Icon, our list of appliances
Nice to have
• Logo on front as big as can be and appliances listed on back of card we carry

```html
<!DOCTYPE html>
<html lang="en">
<head>
<meta charset="utf-8">
<title>Patio Haven Appliances – Business Card</title>
<link rel="stylesheet" href="https://fonts.googleapis.com/css2?family=Poppins:wght@300;400;500;600;700&display=swap">
<style>
  :root {
    --brand-blue: #3c62ad;
    --ink: #111111;
    --paper: #ffffff;
    --page: #e8eae9;
    --muted: #333333;
  }
  html, body {
    margin: 0;
    padding: 0;
    width: 1123px;
    height: 1200px;
    overflow: hidden;
    background: var(--page);
    font-family: "Poppins", sans-serif;
  }
  .sheet {
    position: relative;
    width: 1123px;
    height: 1200px;
  }
  .card {
    position: absolute;
    left: 81px;
    width: 960px;
    height: 549px;
    background: var(--paper);
    box-shadow: 0 6px 18px rgba(0,0,0,0.12);
  }
  .card--front { top: 40px; }
  .card--back { top: 614px; }
  .card svg { display: block; width: 100%; height: 100%; }
  .blue { fill: var(--brand-blue); }
  .white { fill: var(--paper); }
  .black { fill: var(--ink); }
  .brand-name { font-family: "Poppins", sans-serif; font-weight: 700; fill: var(--ink); }
  .tagline { font-family: "Poppins", sans-serif; font-weight: 600; fill: var(--ink); letter-spacing: 1px; }
  .front-phone { font-weight: 400; fill: var(--paper); letter-spacing: 8px; }
  .front-line { font-weight: 400; fill: var(--paper); }
  .person-first { font-weight: 700; fill: var(--ink); }
  .person-last { font-weight: 700; fill: var(--brand-blue); }
  .person-role { font-weight: 300; fill: var(--muted); }
  .brand-list { font-weight: 400; fill: var(--muted); }
  .contact-line { font-weight: 400; fill: var(--ink); }
  .social-handle { font-weight: 400; fill: var(--ink); }
</style>
</head>
<body>
<main class="sheet">

  <section class="card card--front" aria-label="Front of business card">
    <svg viewBox="0 0 790 452" preserveAspectRatio="none" font-family="Poppins, sans-serif">
      <rect class="blue" x="0" y="318" width="790" height="134"/>
      <path class="blue" d="M708 0 L790 0 L790 318 L652 318 L546 200 Q534 186 546 172 Z"/>
      <path class="white" d="M790 95 L716 175 Q704 188 716 201 L790 282 Z"/>
      <path class="black" d="M790 118 L742 174 Q731 187 742 200 L790 258 Z"/>

      <g class="brand-block">
        <rect class="blue" x="128" y="120" width="22" height="22"/>
        <text class="brand-name" x="160" y="142" font-size="40">PATIO HAVEN</text>
        <text class="tagline" x="161" y="182" font-size="19">YOUR APPLIANCE DEALER</text>
      </g>

      <g class="front-contact">
        <path class="white" transform="translate(243 357)" d="M3 1 L7 0 L9 5 L6.5 7 Q8 11 11.5 13 L13.5 10.5 L18 12.5 L17 16.5 Q10 17 5 12 Q0 7 3 1 Z"/>
        <text class="front-phone" x="267" y="374" font-size="21">555 302 1186</text>

        <rect class="white" x="115" y="397" width="13" height="9" rx="1"/>
        <path d="M115 397 L121.5 403 L128 397" fill="none" stroke="#3c62ad" stroke-width="1.2"/>
        <text class="front-line" x="132" y="407" font-size="16">info@patiohavenqx.com</text>

        <path class="white" transform="translate(364 393)" d="M6 0 Q12 0 12 6 Q12 10 6 16 Q0 10 0 6 Q0 0 6 0 Z M6 3.5 A2.5 2.5 0 1 0 6.01 3.5 Z"/>
        <text class="front-line" x="380" y="407" font-size="16">87 Corvale Avenue Fernbrook, QX 11598</text>
      </g>
    </svg>
  </section>

  <section class="card card--back" aria-label="Back of business card">
    <svg viewBox="0 0 795 452" preserveAspectRatio="none" font-family="Poppins, sans-serif">
      <path class="blue" d="M640 0 L795 0 L795 452 L565 452 L385 262 Q370 246 385 230 Z"/>
      <path class="white" d="M795 80 L626 235 Q613 248 626 261 L795 418 Z"/>
      <path class="black" d="M795 140 L686 255 Q675 268 686 281 L795 395 Z"/>

      <rect class="white" x="482" y="172" width="84" height="84" rx="6" role="img" aria-label="QTR accreditation badge"/>

      <g class="social">
        <rect class="white" x="555" y="398" width="142" height="24" rx="5"/>
        <circle class="blue" cx="578" cy="410" r="7"/>
        <text class="social-handle" x="592" y="414" font-size="10">/patiohaven</text>
      </g>

      <text x="48" y="80" font-size="31"><tspan class="person-first">PERSON </tspan><tspan class="person-last">NAME</tspan></text>
      <text class="person-role" x="48" y="105" font-size="19">Chief Executive</text>

      <rect class="blue" x="5" y="168" width="35" height="284"/>

      <g class="brand-list" font-size="14.5">
        <text class="brand-list" x="48" y="234">Orvo, ZRE, Kelu, Quilo, Varno, Kestel,</text>
        <text class="brand-list" x="48" y="260">Stonewick, Bellardi, Gallivant, Ember Charm,</text>
        <text class="brand-list" x="48" y="286">Gray Whitfield, Coastal Blaze, Silver Herons</text>
      </g>

      <rect class="black" x="27" y="347" width="30" height="130" rx="15"/>
      <path class="white" transform="translate(37 360) scale(0.65)" d="M3 1 L7 0 L9 5 L6.5 7 Q8 11 11.5 13 L13.5 10.5 L18 12.5 L17 16.5 Q10 17 5 12 Q0 7 3 1 Z"/>
      <rect class="white" x="37" y="390" width="11" height="8" rx="1"/>
      <path d="M37 390 L42.5 395 L48 390" fill="none" stroke="#111111" stroke-width="1"/>
      <path class="white" transform="translate(38 413) scale(0.8)" d="M6 0 Q12 0 12 6 Q12 10 6 16 Q0 10 0 6 Q0 0 6 0 Z M6 3.5 A2.5 2.5 0 1 0 6.01 3.5 Z"/>

      <text class="contact-line" x="64" y="372" font-size="15.5">555 302 1186</text>
      <text class="contact-line" x="64" y="400" font-size="15.5">info@patiohavenqx.com</text>
      <text class="contact-line" x="64" y="427" font-size="15.5">87 Corvale Avenue Fernbrook, QX 11598</text>
    </svg>
  </section>

</main>
</body>
</html>
```